Bramblewick Co Leaflet. A5 2-sided Flyer for a UK Lawn Treatment Company

I need an A5 two-side leaflet / flyer designed for my Lawn Treatment company. The leaflet will be for door-drops so quick impact needed. Full colour, both sides. I provide lawn treatments to customers in the Exeter area of Devon. I would like to design to be clear, fresh and reflect the joy a good lawn and garden can bring.

Target Market(s)

Home Owners. 30-80 Years. Familys

Font styles to use
Sans Serif

Colors
9bcb3c
f78f20
ec1f27
33a6d7

Requirements
Must have
• Good front page picture
• Logo
• Contact details on front.
• Call to Action
• More details in Text file included in design.
Nice to have
• Clipart of a family / lady enjoying a lawn.

```html
<!DOCTYPE html>
<html lang="en">
<head>
<meta charset="utf-8">
<title>Bramblewick Co Leaflet</title>
<link href="https://fonts.googleapis.com/css2?family=Roboto:wght@400;500;700&family=Roboto+Slab:wght@400;700&family=Lato:wght@400;700&display=swap" rel="stylesheet">
<style>
  :root{
    --bg:#d2dbd9;
    --green:#46e019;
    --green-deep:#2f9a2a;
    --orange:#f47b10;
    --ink:#2b2b2b;
    --title:#2c3436;
    --white:#ffffff;
  }
  *{margin:0;padding:0;box-sizing:border-box}
  html,body{width:1200px;height:1200px;overflow:hidden;background:var(--bg)}
  body{position:relative;font-family:"Lato",sans-serif;color:var(--ink)}
  .side-title{position:absolute;top:206px;width:200px;text-align:center;font:700 32px "Roboto",sans-serif;color:var(--title)}
  .side-title.front{left:215px}
  .side-title.back{left:785px}
  .page{position:absolute;top:270px;width:571px;height:810px;background:var(--white);transform:scale(0.8);transform-origin:0 0;overflow:hidden}
  .page.front{left:98px}
  .page.back{left:647px}
  .page>svg.art{position:absolute;left:0;top:0}
  .abs{position:absolute}
  .brand{left:30px;top:60px;width:180px;text-align:center}
  .brand-mark{width:22px;height:22px;border-radius:50%;background:var(--green-deep);margin:0 auto 8px}
  .brand-name{font:500 25px "Roboto",sans-serif;color:var(--green-deep);white-space:nowrap}
  .tagline{right:13px;top:24px;text-align:right;color:var(--white);font-family:"Roboto Slab",serif}
  .tagline .t1{font-size:25px;line-height:30px}
  .tagline .t2{font-size:18px;line-height:20px}
  .ribbon{left:0;color:var(--white);font:500 16px "Roboto",sans-serif;padding:0 12px 0 14px;display:flex;align-items:center}
  .ribbon.new{top:297px;height:30px;width:200px;background:var(--green-deep);font-size:17px}
  .ribbon.guarantee{top:327px;height:27px;width:265px;background:var(--orange)}
  .intro-head{left:52px;top:565px;font:500 16px "Roboto",sans-serif;color:var(--orange)}
  .intro-text{left:52px;top:591px;width:500px;font-size:11.5px;line-height:15px}
  .services{top:632px;list-style:none;font:500 16px "Roboto",sans-serif;color:#222}
  .services li{display:flex;align-items:center;height:19.7px}
  .services svg{width:11px;height:11px;margin-right:10px}
  .services.col-a{left:52px}
  .services.col-b{left:280px}
  .footer{left:0;top:752px;height:58px;width:571px;color:var(--white);font:500 16px "Roboto",sans-serif}
  .footer .contact{position:absolute;top:16px;display:flex;align-items:center}
  .footer .contact svg{width:15px;height:15px;margin-right:12px}
  .footer .web{position:absolute;left:392px;top:8px;width:140px;text-align:center;line-height:20px}
  .footer .web svg{display:block;margin:0 auto 3px;width:18px;height:18px}
  .section{left:24px;width:524px}
  .section h3{font:500 13px "Roboto",sans-serif;color:var(--orange);text-decoration:underline;display:flex;align-items:center}
  .section h3 span{text-decoration:none;display:inline-block;margin-right:10px;font-weight:700}
  .section p{margin:10px 0 0 16px;font-size:10.4px;line-height:13.5px;text-align:justify}
  .testimonials{left:53px;top:390px;width:467px}
  .testimonials h4{font:500 13.5px "Roboto",sans-serif;color:var(--orange);margin-bottom:6px}
  .testimonials p{font-size:10.3px;line-height:13px;margin-bottom:13px;text-align:justify}
  .testimonials b{color:var(--green-deep)}
  .quote{font:700 60px "Roboto Slab",serif;color:var(--orange);line-height:1}
</style>
</head>
<body>
  <div class="side-title front">Front</div>
  <div class="side-title back">Back</div>

  <section class="page front">
    <svg class="art" width="571" height="810" viewBox="0 0 571 810">
      <defs>
        <linearGradient id="frontPhotoTone" x1="0" y1="0" x2="0" y2="1">
          <stop offset="0" stop-color="#3f8a2a"/><stop offset="0.55" stop-color="#5aa637"/><stop offset="1" stop-color="#7fd33a"/>
        </linearGradient>
        <linearGradient id="lawnTone" x1="0" y1="0" x2="0" y2="1">
          <stop offset="0" stop-color="#3d7a2e"/><stop offset="1" stop-color="#8fdc3a"/>
        </linearGradient>
      </defs>
      <path d="M205,0 C250,75 340,108 450,116 C520,121 560,140 571,160 L571,0Z" fill="var(--green)"/>
      <path d="M205,0 C250,75 340,108 450,116 C520,121 560,140 571,160" fill="none" stroke="var(--orange)" stroke-width="3"/>
      <path role="img" aria-label="Photo of a striped lawn with a gravel path, tall trees and a white garden seat" d="M0,175 C140,120 300,100 430,116 C510,126 560,148 571,175 L571,545 C470,530 400,505 330,480 C240,450 140,440 0,462Z" fill="url(#frontPhotoTone)"/>
      <path d="M0,470 C120,445 230,450 330,485 C420,515 490,545 571,535 L571,548 C490,556 420,530 330,498 C230,462 120,462 0,482Z" fill="var(--orange)"/>
      <circle cx="123" cy="470" r="76" fill="#fff"/>
      <circle role="img" aria-label="Photo of a bright green garden lawn" cx="123" cy="470" r="73" fill="url(#lawnTone)"/>
      <circle cx="293" cy="485" r="70" fill="#fff"/>
      <circle role="img" aria-label="Photo of a lawn bordered by shrubs" cx="293" cy="485" r="67" fill="url(#lawnTone)"/>
      <path d="M571,655 C555,700 520,725 470,735 L571,735Z" fill="var(--green)"/>
      <path d="M571,655 C555,700 520,725 470,735" fill="none" stroke="var(--orange)" stroke-width="5"/>
      <path d="M318,810 C360,760 400,735 470,735 L571,735 L571,810Z" fill="var(--green)"/>
    </svg>

    <div class="abs brand">
      <div class="brand-mark"></div>
      <div class="brand-name">Bramblewick Co</div>
    </div>
    <div class="abs tagline">
      <div class="t1">Treatments and advice</div>
      <div class="t2">to keep your lawn looking nice</div>
    </div>
    <div class="abs ribbon new">Brand new to the area!</div>
    <div class="abs ribbon guarantee">Complete Satisfaction Guarantee</div>

    <h2 class="abs intro-head">Industry-Leading Lawn Care</h2>
    <p class="abs intro-text">I have 8 years of experience in the leading edge of domestic lawn care. I have a comprehensive range of treatments including:</p>
    <ul class="abs services col-a">
      <li><svg viewBox="0 0 12 12"><path d="M1,6 L4.5,9.5 L11,2" fill="none" stroke="var(--orange)" stroke-width="2"/></svg>Scarification</li>
      <li><svg viewBox="0 0 12 12"><path d="M1,6 L4.5,9.5 L11,2" fill="none" stroke="var(--orange)" stroke-width="2"/></svg>Aeration</li>
      <li><svg viewBox="0 0 12 12"><path d="M1,6 L4.5,9.5 L11,2" fill="none" stroke="var(--orange)" stroke-width="2"/></svg>Moss Control</li>
      <li><svg viewBox="0 0 12 12"><path d="M1,6 L4.5,9.5 L11,2" fill="none" stroke="var(--orange)" stroke-width="2"/></svg>Overseeding</li>
      <li><svg viewBox="0 0 12 12"><path d="M1,6 L4.5,9.5 L11,2" fill="none" stroke="var(--orange)" stroke-width="2"/></svg>Top Dressing</li>
    </ul>
    <ul class="abs services col-b">
      <li><svg viewBox="0 0 12 12"><path d="M1,6 L4.5,9.5 L11,2" fill="none" stroke="var(--orange)" stroke-width="2"/></svg>Lawn Repairs</li>
      <li><svg viewBox="0 0 12 12"><path d="M1,6 L4.5,9.5 L11,2" fill="none" stroke="var(--orange)" stroke-width="2"/></svg>Fertilisation &amp; Weed Control</li>
      <li><svg viewBox="0 0 12 12"><path d="M1,6 L4.5,9.5 L11,2" fill="none" stroke="var(--orange)" stroke-width="2"/></svg>Pest and Disease Management</li>
      <li><svg viewBox="0 0 12 12"><path d="M1,6 L4.5,9.5 L11,2" fill="none" stroke="var(--orange)" stroke-width="2"/></svg>Special Event Preparation</li>
    </ul>

    <div class="abs footer">
      <svg class="abs" width="571" height="58" viewBox="0 0 571 58" style="left:0;top:0"><path d="M0,0 L372,0 C350,18 330,35 318,58 L0,58Z" fill="var(--orange)"/></svg>
      <div class="contact" style="left:24px"><svg viewBox="0 0 16 16"><path d="M3,1 L6,1 L7,5 L5,6.5 C6,9 7,10 9.5,11 L11,9 L15,10 L15,13 C15,14 14,15 13,15 C6,14 2,10 1,3 C1,2 2,1 3,1Z" fill="#fff"/></svg>01632 960418</div>
      <div class="contact" style="left:183px"><svg viewBox="0 0 16 16"><rect x="1" y="3" width="14" height="10" fill="#fff"/><path d="M1,3 L8,9 L15,3" fill="none" stroke="var(--orange)" stroke-width="1.5"/></svg>07700 900417</div>
      <div class="web"><svg viewBox="0 0 18 18"><g fill="none" stroke="#fff" stroke-width="1.3"><circle cx="9" cy="9" r="7.5"/><ellipse cx="9" cy="9" rx="3.2" ry="7.5"/><path d="M1.5,9 H16.5 M3,5 H15 M3,13 H15"/></g></svg>bramblewickco.co.uk</div>
    </div>
  </section>

  <section class="page back">
    <svg class="art" width="571" height="810" viewBox="0 0 571 810">
      <defs>
        <linearGradient id="backPhotoTone" x1="0" y1="0" x2="0" y2="1">
          <stop offset="0" stop-color="#2f6b24"/><stop offset="0.6" stop-color="#4f9a30"/><stop offset="1" stop-color="#86d83a"/>
        </linearGradient>
        <radialGradient id="dropTone" cx="0.45" cy="0.45" r="0.6">
          <stop offset="0" stop-color="#c8f56a"/><stop offset="0.6" stop-color="#5fd31d"/><stop offset="1" stop-color="#2f9a14"/>
        </radialGradient>
      </defs>
      <path role="img" aria-label="Photo of a wide striped lawn among trees and flower borders" d="M0,0 L571,0 L571,142 C480,160 420,150 330,168 C230,185 100,175 0,150Z" fill="url(#backPhotoTone)"/>
      <path d="M0,150 C100,175 230,185 330,168 C420,150 480,160 571,142" fill="none" stroke="var(--green)" stroke-width="4"/>
      <circle cx="424" cy="127" r="78" fill="#fff"/>
      <circle role="img" aria-label="Close-up photo of a water droplet on a grass blade" cx="424" cy="127" r="74" fill="url(#dropTone)"/>
      <g fill="none" stroke="var(--green)" stroke-width="3">
        <path d="M40,384 L472,384"/>
        <path d="M37,384 L37,697"/>
        <path d="M534,415 L534,680 C534,692 525,697 515,697 L100,697"/>
      </g>
      <path d="M571,660 C555,710 520,725 485,732 L571,732Z" fill="var(--green)"/>
      <path d="M571,660 C555,710 520,725 485,732" fill="none" stroke="var(--orange)" stroke-width="5"/>
      <path d="M318,810 C360,758 410,735 485,732 L571,732 L571,810Z" fill="var(--green)"/>
    </svg>

    <div class="abs section" style="top:194px">
      <h3><span>›</span>For a Beautiful Weed-Free Lawn</h3>
      <p>Call Bramblewick Co today and start your journey to a wonderful, lush, green lawn you and your family can enjoy. Arrange a no-obligation lawn survey and quotation at a time to suit you.</p>
    </div>
    <div class="abs section" style="top:255px">
      <h3><span>›</span>I will Understand Your Lawn</h3>
      <p>Every lawn is unique. I take time to gain a comprehensive understanding of your lawn and its situation. I will also listen to you and understand your problems and your aspirations for your grass.</p>
    </div>
    <div class="abs section" style="top:316px">
      <h3><span>›</span>Your Lawn Treatments</h3>
      <p>I will creat a custom treatment programme tailored to your lawn. I may also recommend some remedial treatments to correct any existing problems. There is no contract to sign. I guarantee all treatments.</p>
    </div>

    <div class="abs quote" style="left:483px;top:366px">”</div>
    <div class="abs quote" style="left:46px;top:676px">“</div>

    <div class="abs testimonials">
      <h4>Testimonials</h4>
      <p>Thank you for keeping our lawn in great shape for so long, I've been really pleased with how it has looked since you took care of it. - <b>Owen</b></p>
      <p>My lawn has never looked better since the day that you started to look after it for me. - <b>Mr. Pell</b></p>
      <p>We are so grateful for your skill over the years. We've seen our lawn thrive and you changed a neglected difficult garden to one that everyone comments on. - <b>Carys</b></p>
      <p>Thank you for the lawn service you have provided over the years. It is reassuring to have you come round as I know you carried out the service as promised unlike other lawn service companies I have dealt with. - <b>Martin</b></p>
      <p>We have very much appreciated your service over the last four years, and especially value your reliability and perennial cheerfulness! - <b>Rowan</b></p>
      <p>It has been a pleasure to do business with you over the last few years and the lawn you leave us with is infinitely healthier and more attractive than the lawn you inherited! - <b>Hazel</b></p>
      <p>Your company have been fantastic. Reliable, good advice, effective treatments and you are very knowledgeable about lawns. You really do know what you are talking about! Cannot recommend you highly enough. - <b>Martin</b></p>
    </div>

    <div class="abs footer">
      <svg class="abs" width="571" height="58" viewBox="0 0 571 58" style="left:0;top:0"><path d="M0,0 L378,0 C355,18 332,36 318,58 L0,58Z" fill="var(--orange)"/></svg>
      <div class="contact" style="left:30px"><svg viewBox="0 0 16 16"><path d="M3,1 L6,1 L7,5 L5,6.5 C6,9 7,10 9.5,11 L11,9 L15,10 L15,13 C15,14 14,15 13,15 C6,14 2,10 1,3 C1,2 2,1 3,1Z" fill="#fff"/></svg>01632 960418</div>
      <div class="contact" style="left:189px"><svg viewBox="0 0 16 16"><rect x="1" y="3" width="14" height="10" fill="#fff"/><path d="M1,3 L8,9 L15,3" fill="none" stroke="var(--orange)" stroke-width="1.5"/></svg>07700 900417</div>
      <div class="web" style="left:388px;top:10px"><svg viewBox="0 0 18 18"><g fill="none" stroke="#fff" stroke-width="1.3"><circle cx="9" cy="9" r="7.5"/><ellipse cx="9" cy="9" rx="3.2" ry="7.5"/><path d="M1.5,9 H16.5 M3,5 H15 M3,13 H15"/></g></svg>bramblewickco.co.uk</div>
    </div>
  </section>
</body>
</html>
```